StayCrewly.com homepage

We need a new homepage for our new domain.

StayCrewly.com

The colors to be used are the ones in our logo (attached) and in the current log in page host.lodgenestly.com

Its important its a ONE PAGE site where you can scroll and elements appear while scrolling down.

It has to be simple to the point similar to the chatterbook log in page.

The current log in box and registration box have to stay but can be moved around obviously.

Also the video as on our current page www.lodgenestly.com needs to have its place on the homepage.

Slogan

StayCrewly.com - The Rental Teamwork Hub.

Vacation rental managers and hosts can now team up with a booking team. Its easy to instantly improve your online booking management. Be on all the best booking sites without all the hassle. Improve your current strategy and save loads of time which you can spend on the satisfaction of your guests.

Something like that not too long.

I look forward to seeing your proposed designs.

In the attachment is our logo and a screenshot of our backend so the design will match nicely

Target Market(s)

Owners and property managers of vacation rentals world wide

Industry/Entity Type

Domain

Number of Pages Required

1 page

Requirements
Nice to have
• Smooth scrolling elements

```html
<!DOCTYPE html>
<html lang="en">
<head>
<meta charset="utf-8">
<title>StayCrewly.com – The Rental Teamwork Hub</title>
<link rel="stylesheet" href="https://fonts.googleapis.com/css2?family=Ubuntu:wght@400;500;700&display=swap">
<style>
  :root {
    --navy: #1d3f8c;
    --navy-box: #0b3a83;
    --orange: #f65a14;
    --grey-text: #555;
    --field-border: #e0c6b8;
    --login-grey: #5b5b5b;
    --partners-bg: #ebebeb;
    --partner-shape: #6c6c6c;
    --works-bg: #7aaad6;
    --footer-bg: #5a5a5a;
    --white: #fff;
  }
  * { box-sizing: border-box; margin: 0; padding: 0; }
  html, body { width: 875px; height: 1200px; overflow: hidden; }
  body { position: relative; font-family: "Ubuntu", sans-serif; background: var(--white); color: #222; }
  .abs { position: absolute; }

  /* Header */
  .site-header { left: 0; top: 0; width: 875px; height: 88px; background: var(--white); border-bottom: 2px solid var(--orange); }
  .brand { left: 46px; top: 24px; display: flex; align-items: center; gap: 8px; font-size: 22px; font-weight: 700; color: var(--navy); }
  .brand-dot { width: 16px; height: 16px; border-radius: 50%; background: var(--orange); }
  .lang-select { left: 724px; top: 8px; width: 116px; height: 20px; border: 1px solid #bbb; font-size: 11px; color: #444; padding: 2px 5px; }
  .lang-select::after { content: "▼"; position: absolute; right: 8px; top: 3px; font-size: 8px; }
  .field { height: 25px; border: 1px solid var(--field-border); background: var(--white); font-size: 11px; color: #bbb; padding: 5px 9px; }
  .user-field { left: 385px; top: 38px; width: 176px; }
  .pass-field { left: 571px; top: 38px; width: 176px; }
  .login-btn { left: 761px; top: 35px; width: 77px; height: 27px; background: var(--login-grey); color: var(--white); font-size: 14px; font-weight: 500; text-align: center; line-height: 27px; border-radius: 2px; }
  .remember { left: 392px; top: 67px; font-size: 11px; color: var(--grey-text); }
  .forgot { left: 574px; top: 66px; font-size: 11px; color: var(--orange); }

  /* Hero */
  .hero { left: 0; top: 90px; width: 875px; height: 531px; background: linear-gradient(115deg, #5c6770 0%, #b7c4d0 35%, #d6dee6 55%, #8f9aa6 80%, #6b7580 100%); }
  .hero-title { left: 0; top: 116px; width: 875px; text-align: center; font-size: 39px; font-weight: 400; color: var(--navy); letter-spacing: 0.5px; }
  .feature { top: 178px; width: 190px; height: 191px; background: rgba(235,240,245,0.45); border: 1px solid rgba(255,255,255,0.6); }
  .feature-icon { position: absolute; left: 75px; top: 9px; width: 40px; height: 40px; }
  .feature p { position: absolute; left: 16px; right: 10px; font-size: 15.5px; line-height: 19px; color: #222; }
  .tagline { left: 0; top: 383px; width: 875px; text-align: center; font-size: 26px; color: var(--white); word-spacing: 6px; }
  .register-box { left: 249px; top: 426px; width: 425px; height: 178px; background: var(--navy-box); border: 1px solid #222; }
  .register-box p { position: absolute; left: 59px; top: 24px; width: 330px; font-size: 12.5px; line-height: 15px; color: var(--white); font-weight: 500; }
  .email-field { position: absolute; left: 63px; top: 71px; width: 266px; height: 32px; background: var(--white); font-size: 12px; color: #aaa; padding: 9px 9px; }
  .register-btn { position: absolute; left: 63px; top: 122px; width: 130px; height: 35px; background: var(--orange); color: var(--white); font-size: 15px; font-weight: 500; text-align: center; line-height: 35px; }

  /* Partners */
  .partners { left: 0; top: 621px; width: 875px; height: 125px; background: var(--partners-bg); }
  .section-title { position: absolute; left: 0; width: 875px; text-align: center; font-size: 26px; color: #333; }
  .partner-row { position: absolute; left: 30px; top: 70px; width: 810px; display: flex; justify-content: space-between; align-items: center; }
  .partner-badge { height: 30px; background: var(--partner-shape); border-radius: 4px; opacity: 0.8; }

  /* How it works */
  .how { left: 0; top: 746px; width: 875px; height: 400px; background: var(--works-bg); }
  .video-frame { position: absolute; left: 174px; top: 79px; width: 559px; height: 276px; background: var(--white); border: 2px solid #d8d8d8; }
  .video-art { position: absolute; left: 20px; top: 6px; width: 515px; height: 225px; background: linear-gradient(180deg, #f6f6f6 0%, #f6f6f6 35%, #c3272f 36%, #a41d26 100%); }
  .player { position: absolute; left: 37px; top: 231px; width: 489px; height: 28px; background: linear-gradient(#eee, #cfcfcf); border: 1px solid #bbb; }

  /* Footer */
  .site-footer { left: 0; top: 1146px; width: 875px; height: 54px; background: var(--footer-bg); border-top: 2px solid var(--orange); text-align: center; font-size: 11px; color: var(--white); padding-top: 21px; }
  .site-footer span { margin: 0 10px; }
</style>
</head>
<body>

<header class="site-header abs">
  <div class="brand abs"><span class="brand-dot"></span>StayCrewly.com</div>
  <div class="lang-select abs">Choose language</div>
  <div class="field user-field abs">Username or email</div>
  <div class="field pass-field abs">Password</div>
  <div class="login-btn abs">Login</div>
  <div class="remember abs">☑&nbsp; Remember me</div>
  <div class="forgot abs">Forgot password</div>
</header>

<section class="hero abs" role="img" aria-label="Blurred photo of a team of colleagues giving each other a high five"></section>
<h1 class="hero-title abs">THE BOOKING COLLABORATION PLATFORM</h1>

<div class="feature abs" style="left:44px">
  <svg class="feature-icon" viewBox="0 0 40 40"><circle cx="20" cy="20" r="19" fill="#fff" stroke="#222" stroke-width="1.3"/><g fill="#222"><circle cx="13" cy="14" r="2.6"/><circle cx="20" cy="13" r="2.8"/><circle cx="27" cy="14" r="2.6"/><rect x="10" y="17.5" width="6" height="10" rx="1.5"/><rect x="17" y="17" width="6" height="11" rx="1.5"/><rect x="24" y="17.5" width="6" height="10" rx="1.5"/></g></svg>
  <p style="top:62px">Vacation rental managers and hosts can now team up with a booking team.</p>
</div>
<div class="feature abs" style="left:248px">
  <svg class="feature-icon" viewBox="0 0 40 40"><circle cx="20" cy="20" r="19" fill="#fff" stroke="#222" stroke-width="1.3"/><rect x="15" y="14" width="10" height="15" rx="5" fill="#222"/><line x1="20" y1="8" x2="20" y2="17" stroke="#222" stroke-width="1.5"/><line x1="15.5" y1="19" x2="24.5" y2="19" stroke="#fff" stroke-width="1"/></svg>
  <p style="top:64px">Its easy to instantly improve your online booking management.</p>
</div>
<div class="feature abs" style="left:451px">
  <svg class="feature-icon" viewBox="0 0 40 40"><circle cx="20" cy="20" r="19" fill="#fff" stroke="#222" stroke-width="1.3"/><circle cx="20" cy="20" r="12" fill="#222"/><circle cx="20" cy="13.5" r="2" fill="#fff"/><path d="M13 17h14M20 17v6l-3.5 6M20 23l3.5 6" stroke="#fff" stroke-width="2" fill="none"/></svg>
  <p style="top:62px">Be on all the best booking sites without all the hassle.</p>
</div>
<div class="feature abs" style="left:655px">
  <svg class="feature-icon" viewBox="0 0 40 40"><circle cx="20" cy="20" r="19" fill="#fff" stroke="#222" stroke-width="1.3"/><circle cx="20" cy="20" r="10" fill="none" stroke="#222" stroke-width="2"/><path d="M20 14v6h5" stroke="#222" stroke-width="2" fill="none"/></svg>
  <p style="top:62px">Improve your current strategy and save loads of time which you can spend on the satisfaction of your guests.</p>
</div>

<div class="tagline abs">TEAM UP SHARE DO BETTER</div>

<div class="register-box abs">
  <p>Join the free booking network with optional personal booking team today</p>
  <div class="email-field">Enter email</div>
  <div class="register-btn">Register</div>
</div>

<section class="partners abs">
  <h2 class="section-title" style="top:19px;font-weight:400">Our partners</h2>
  <div class="partner-row">
    <div class="partner-badge" style="width:122px"></div>
    <div class="partner-badge" style="width:140px"></div>
    <div class="partner-badge" style="width:106px"></div>
    <div class="partner-badge" style="width:76px;height:38px"></div>
    <div class="partner-badge" style="width:122px"></div>
    <div class="partner-badge" style="width:164px"></div>
  </div>
</section>

<section class="how abs">
  <h2 class="section-title" style="top:34px;font-weight:400">How it works</h2>
  <div class="video-frame">
    <div class="video-art" role="img" aria-label="Explainer video frame, step one: share bookings and services on the social platform, with a red greetings illustration"></div>
    <div class="player">
      <svg width="489" height="28" viewBox="0 0 489 28">
        <path d="M14 8l12 6-12 6z" fill="#444"/>
        <line x1="38" y1="4" x2="38" y2="24" stroke="#bbb"/>
        <rect x="50" y="10" width="247" height="7" rx="3.5" fill="#666"/>
        <rect x="50" y="10" width="165" height="7" rx="3.5" fill="#e8445a"/>
        <rect x="50" y="10" width="165" height="3" rx="1.5" fill="#f59aa6"/>
        <circle cx="164" cy="13.5" r="5" fill="#ddd" stroke="#888"/>
        <text x="339" y="18" font-family="Ubuntu, sans-serif" font-size="10" fill="#333">3.47 / 9.29</text>
        <line x1="400" y1="4" x2="400" y2="24" stroke="#bbb"/>
        <path d="M412 11h4l5-4v14l-5-4h-4z" fill="#555"/>
        <rect x="436" y="10" width="66" height="7" rx="3.5" fill="#666"/>
        <circle cx="496" cy="13.5" r="4.5" fill="#ddd" stroke="#888"/>
        <line x1="510" y1="4" x2="510" y2="24" stroke="#bbb"/>
      </svg>
      <svg class="abs" style="left:460px;top:7px" width="14" height="14" viewBox="0 0 14 14"><rect x="1" y="1" width="12" height="12" fill="none" stroke="#444" stroke-width="1.5"/><rect x="4" y="4" width="6" height="6" fill="#444"/></svg>
    </div>
  </div>
</section>

<footer class="site-footer abs">
  <span>Terms and conditions</span>|<span>Contact us</span>|<span>About us</span>
</footer>

</body>
</html>
```